Simple, clean boat charter Banners

We need a variety of banner designs for our charter boat company. We provide boat trips to hollis bank, beaches and snorkeling. You can see our site www.meridelboats.com to get a better idea of our image.

We need the banner to be clean, simple and pleasing to the eye. The following ad dimensions we need are:

300 x 250
336 x 280
728 x 90
300 x 600
320 x 100

I've included a range of photos and logos to pic from.

Ignore the logo in all the photos. If a portion of the logo in the photo is in the banner, down worry. I will proved photos with the logo removed for the winning designs.

Please include a phrase, such as the following:
- Private Boat Charters to Hollis Bank
- Private Boat Charters in Grand Cayman

If you can think of fun witty phrases, feel free to try them out. We are very open to creative ideas!! For example:
- Come visit the stingrays with us!
- Have you ever kissed a stingray?

Target Market(s)

Up-scale 30-50 year olds residing in North America

Industry/Entity Type

Tourism

Colors
3176b5
0655a3
85cae6
33a6d7
0592cd
cee9f5

Requirements
Nice to have
• Clean, Simple, Modern

```html
<!DOCTYPE html>
<html lang="en">
<head>
<meta charset="utf-8">
<title>Meridel Boats – Banner Set</title>
<link rel="stylesheet" href="https://fonts.googleapis.com/css2?family=Oswald:wght@300;400;600&display=swap">
<style>
:root{
  --stage:#1c1c1d;
  --blue-top:#1f79bf;
  --blue-mid:#0a5fae;
  --blue-deep:#0655a3;
  --sky:#85cae6;
  --ice:#cee9f5;
  --white:#ffffff;
  --head-top:#ffffff;
  --head-bot:#d6dbe1;
  --brand:#0655a3;
  --btn-top:#ffc21a;
  --btn-bot:#f08a00;
  --btn-edge:#ffd97a;
  --btn-ink:#2b1a00;
  --pool-a:#7fe3f2;--pool-b:#22b6dc;--pool-c:#1583b8;
  --sea-a:#8fd3e8;--sea-b:#2bc1c4;--sea-c:#1b8fa0;
  --reef-a:#3e9c8a;--reef-b:#1e7a68;--reef-c:#135a4c;
}
*{margin:0;padding:0;box-sizing:border-box}
html,body{width:1200px;height:1200px;overflow:hidden;background:var(--stage)}
body{font-family:"Oswald",sans-serif}
.stage{position:relative;width:1500px;height:1500px;transform:scale(.8);transform-origin:0 0}

.banner{position:absolute;overflow:hidden;background:linear-gradient(180deg,var(--blue-top),var(--blue-mid) 60%,var(--blue-deep));color:var(--white);box-shadow:0 2px 8px rgba(0,0,0,.6)}
.header{position:absolute;left:0;top:0;right:0;background:linear-gradient(180deg,var(--head-top),var(--head-bot))}
.brand{position:absolute;display:flex;align-items:center;justify-content:center;gap:6px;color:var(--brand);font-weight:400;letter-spacing:2px;white-space:nowrap}
.brand-dot{width:9px;height:9px;border-radius:50%;background:var(--brand)}
.photo{position:absolute}
.ph-pool{background:radial-gradient(ellipse at 40% 30%,var(--pool-a),var(--pool-b) 55%,var(--pool-c))}
.ph-boat{background:linear-gradient(180deg,var(--sky) 0%,var(--ice) 28%,var(--sea-b) 42%,var(--sea-c) 100%)}
.ph-reef{background:linear-gradient(180deg,#9ab8c8 0%,#d6e2e8 18%,var(--reef-a) 32%,var(--reef-b) 65%,var(--reef-c))}

.copy{position:absolute;text-align:center;letter-spacing:-.5px}
.copy .light,.copy .bold,.copy .sub{white-space:nowrap}
.copy .light{font-weight:300;display:block;text-transform:uppercase}
.copy .bold{font-weight:600;display:block;text-transform:uppercase}
.copy .sub{display:block;font-weight:300}
.cta{display:inline-flex;align-items:center;gap:6px;background:linear-gradient(180deg,var(--btn-top),var(--btn-bot));border:1px solid var(--btn-edge);border-radius:3px;color:var(--btn-ink);font-weight:400;text-transform:uppercase;letter-spacing:-.3px;padding:0 10px;box-shadow:0 1px 3px rgba(0,0,0,.35);white-space:nowrap}
.cta svg{flex:none}

/* 336 x 280 */
.rect-l{width:340px;height:282px}
.rect-l .header{height:78px}
.rect-l .brand{left:0;width:200px;top:28px;font-size:19px}
.rect-l .photo{inset:0;clip-path:path("M220 0 L340 0 L340 282 L172 282 Q178 120 220 0 Z")}
.rect-l .copy{left:0;top:84px;width:182px}
.rect-l .light,.rect-l .bold{font-size:26px;line-height:26px}
.rect-l .sub{font-size:19px;line-height:21px;margin:12px 0 8px}
.rect-l .cta{height:32px;font-size:18px}

/* 320 x 265 */
.rect-s{width:320px;height:265px}
.rect-s .header{height:74px}
.rect-s .brand{left:0;width:180px;top:27px;font-size:17px}
.rect-s .photo{inset:0;clip-path:path("M205 0 L320 0 L320 265 L160 265 Q166 112 205 0 Z")}
.rect-s .copy{left:0;top:80px;width:166px}
.rect-s .light,.rect-s .bold{font-size:24px;line-height:25px}
.rect-s .sub{font-size:18px;line-height:20px;margin:10px 0 7px}
.rect-s .cta{height:30px;font-size:17px}

/* 300 x 600 */
.tall{width:300px;height:600px}
.tall .header{height:95px}
.tall .brand{left:0;right:0;top:34px;font-size:26px;letter-spacing:4px}
.tall .photo{left:0;top:298px;width:300px;height:302px;clip-path:path("M0 60 Q120 -8 300 2 L300 302 L0 302 Z")}
.tall .copy{left:0;right:0;top:102px}
.tall .light,.tall .bold{font-size:34px;line-height:34px}
.tall .sub{font-size:20px;line-height:22px;margin:14px 0 8px}
.tall .cta{height:34px;font-size:19px}

/* 728 x 90 */
.board{width:728px;height:90px}
.board .header{width:158px;right:auto;height:90px}
.board .brand{left:0;width:158px;top:34px;font-size:16px}
.board .photo{left:415px;top:0;width:313px;height:90px;clip-path:path("M20 0 L313 0 L313 90 L0 90 Q2 40 20 0 Z")}
.board .copy{left:160px;top:7px;width:244px}
.board .bold,.board .light{font-size:25px;line-height:27px}
.board .sub{font-size:17px;line-height:20px}
.board .cta{position:absolute;right:5px;top:30px;height:30px;font-size:17px}

/* 320 x 100 */
.mini{width:320px;height:100px}
.mini .photo{left:152px;top:0;width:168px;height:100px;clip-path:path("M20 0 L168 0 L168 100 L0 100 Q4 45 20 0 Z")}
.mini .copy{left:2px;top:10px;width:152px}
.mini .light,.mini .bold{font-size:23px;line-height:26px}
</style>
</head>
<body>
<div class="stage">

  <div class="banner rect-l" style="left:190px;top:51px">
    <div class="header"></div>
    <div class="photo ph-pool" role="img" aria-label="Family snorkeling underwater in clear turquoise water"></div>
    <div class="brand"><span class="brand-dot"></span>MERIDEL BOATS</div>
    <div class="copy"><span class="light">Private Boat</span><span class="bold">Charters in</span><span class="bold">Grand Cayman</span><span class="sub">Come visit the<br>stingrays with us!</span><span class="cta">Learn More <svg width="14" height="14" viewBox="0 0 14 14"><circle cx="7" cy="7" r="7" fill="#2b1a00"/><path d="M3.5 7h6M7 4.5 9.5 7 7 9.5" stroke="#fff" stroke-width="1.8" fill="none"/></svg></span></div>
  </div>
  <div class="banner rect-l" style="left:580px;top:51px">
    <div class="header"></div>
    <div class="photo ph-boat" role="img" aria-label="Charter boat anchored in shallow turquoise sea"></div>
    <div class="brand"><span class="brand-dot"></span>MERIDEL BOATS</div>
    <div class="copy"><span class="light">Private Boat</span><span class="bold">Charters in</span><span class="bold">Grand Cayman</span><span class="sub">Come visit the<br>stingrays with us!</span><span class="cta">Learn More <svg width="14" height="14" viewBox="0 0 14 14"><circle cx="7" cy="7" r="7" fill="#2b1a00"/><path d="M3.5 7h6M7 4.5 9.5 7 7 9.5" stroke="#fff" stroke-width="1.8" fill="none"/></svg></span></div>
  </div>
  <div class="banner rect-l" style="left:967px;top:54px">
    <div class="header"></div>
    <div class="photo ph-reef" role="img" aria-label="Snorkelers over a green reef near the shore"></div>
    <div class="brand"><span class="brand-dot"></span>MERIDEL BOATS</div>
    <div class="copy"><span class="light">Private Boat</span><span class="bold">Charters in</span><span class="bold">Grand Cayman</span><span class="sub">Come visit the<br>stingrays with us!</span><span class="cta">Learn More <svg width="14" height="14" viewBox="0 0 14 14"><circle cx="7" cy="7" r="7" fill="#2b1a00"/><path d="M3.5 7h6M7 4.5 9.5 7 7 9.5" stroke="#fff" stroke-width="1.8" fill="none"/></svg></span></div>
  </div>

  <div class="banner rect-s" style="left:66px;top:393px">
    <div class="header"></div>
    <div class="photo ph-pool" role="img" aria-label="Family snorkeling underwater in clear turquoise water"></div>
    <div class="brand"><span class="brand-dot"></span>MERIDEL BOATS</div>
    <div class="copy"><span class="light">Private Boat</span><span class="bold">Charters in</span><span class="bold">Grand Cayman</span><span class="sub">Come visit the<br>stingrays with us!</span><span class="cta">Learn More <svg width="13" height="13" viewBox="0 0 14 14"><circle cx="7" cy="7" r="7" fill="#2b1a00"/><path d="M3.5 7h6M7 4.5 9.5 7 7 9.5" stroke="#fff" stroke-width="1.8" fill="none"/></svg></span></div>
  </div>
  <div class="banner rect-s" style="left:66px;top:694px">
    <div class="header"></div>
    <div class="photo ph-reef" role="img" aria-label="Snorkelers over a green reef near the shore"></div>
    <div class="brand"><span class="brand-dot"></span>MERIDEL BOATS</div>
    <div class="copy"><span class="light">Private Boat</span><span class="bold">Charters in</span><span class="bold">Grand Cayman</span><span class="sub">Come visit the<br>stingrays with us!</span><span class="cta">Learn More <svg width="13" height="13" viewBox="0 0 14 14"><circle cx="7" cy="7" r="7" fill="#2b1a00"/><path d="M3.5 7h6M7 4.5 9.5 7 7 9.5" stroke="#fff" stroke-width="1.8" fill="none"/></svg></span></div>
  </div>
  <div class="banner rect-s" style="left:66px;top:990px">
    <div class="header"></div>
    <div class="photo ph-boat" role="img" aria-label="Charter boat anchored in shallow turquoise sea"></div>
    <div class="brand"><span class="brand-dot"></span>MERIDEL BOATS</div>
    <div class="copy"><span class="light">Private Boat</span><span class="bold">Charters in</span><span class="bold">Grand Cayman</span><span class="sub">Come visit the<br>stingrays with us!</span><span class="cta">Learn More <svg width="13" height="13" viewBox="0 0 14 14"><circle cx="7" cy="7" r="7" fill="#2b1a00"/><path d="M3.5 7h6M7 4.5 9.5 7 7 9.5" stroke="#fff" stroke-width="1.8" fill="none"/></svg></span></div>
  </div>

  <div class="banner tall" style="left:440px;top:370px">
    <div class="header"></div>
    <div class="brand"><span class="brand-dot"></span>MERIDEL BOATS</div>
    <div class="copy"><span class="light">Private Boat</span><span class="bold">Charters in</span><span class="bold">Grand Cayman</span><span class="sub">Come visit the stingrays with us!</span><span class="cta">Learn More <svg width="14" height="14" viewBox="0 0 14 14"><circle cx="7" cy="7" r="7" fill="#2b1a00"/><path d="M3.5 7h6M7 4.5 9.5 7 7 9.5" stroke="#fff" stroke-width="1.8" fill="none"/></svg></span></div>
    <div class="photo ph-pool" role="img" aria-label="Family snorkeling underwater in clear turquoise water"></div>
  </div>
  <div class="banner tall" style="left:770px;top:370px">
    <div class="header"></div>
    <div class="brand"><span class="brand-dot"></span>MERIDEL BOATS</div>
    <div class="copy"><span class="light">Private Boat</span><span class="bold">Charters in</span><span class="bold">Grand Cayman</span><span class="sub">Come visit the stingrays with us!</span><span class="cta">Learn More <svg width="14" height="14" viewBox="0 0 14 14"><circle cx="7" cy="7" r="7" fill="#2b1a00"/><path d="M3.5 7h6M7 4.5 9.5 7 7 9.5" stroke="#fff" stroke-width="1.8" fill="none"/></svg></span></div>
    <div class="photo ph-boat" role="img" aria-label="Charter boat anchored in shallow turquoise sea"></div>
  </div>
  <div class="banner tall" style="left:1101px;top:371px">
    <div class="header"></div>
    <div class="brand"><span class="brand-dot"></span>MERIDEL BOATS</div>
    <div class="copy"><span class="light">Private Boat</span><span class="bold">Charters in</span><span class="bold">Grand Cayman</span><span class="sub">Come visit the stingrays with us!</span><span class="cta">Learn More <svg width="14" height="14" viewBox="0 0 14 14"><circle cx="7" cy="7" r="7" fill="#2b1a00"/><path d="M3.5 7h6M7 4.5 9.5 7 7 9.5" stroke="#fff" stroke-width="1.8" fill="none"/></svg></span></div>
    <div class="photo ph-reef" role="img" aria-label="Snorkelers over a green reef near the shore"></div>
  </div>

  <div class="banner board" style="left:539px;top:1006px">
    <div class="header"></div>
    <div class="brand"><span class="brand-dot"></span>MERIDEL BOATS</div>
    <div class="photo ph-pool" role="img" aria-label="Family snorkeling underwater in clear turquoise water"></div>
    <div class="copy"><span class="bold">Private Boat Charters</span><span class="light">In Grand Cayman</span><span class="sub">Come visit the stingrays with us!</span></div>
    <span class="cta">Learn More <svg width="13" height="13" viewBox="0 0 14 14"><circle cx="7" cy="7" r="7" fill="#2b1a00"/><path d="M3.5 7h6M7 4.5 9.5 7 7 9.5" stroke="#fff" stroke-width="1.8" fill="none"/></svg></span>
  </div>
  <div class="banner board" style="left:539px;top:1116px">
    <div class="header"></div>
    <div class="brand"><span class="brand-dot"></span>MERIDEL BOATS</div>
    <div class="photo ph-reef" role="img" aria-label="Snorkelers swimming over a green reef"></div>
    <div class="copy"><span class="bold">Private Boat Charters</span><span class="light">In Grand Cayman</span><span class="sub">Come visit the stingrays with us!</span></div>
    <span class="cta">Learn More <svg width="13" height="13" viewBox="0 0 14 14"><circle cx="7" cy="7" r="7" fill="#2b1a00"/><path d="M3.5 7h6M7 4.5 9.5 7 7 9.5" stroke="#fff" stroke-width="1.8" fill="none"/></svg></span>
  </div>
  <div class="banner board" style="left:540px;top:1224px">
    <div class="header"></div>
    <div class="brand"><span class="brand-dot"></span>MERIDEL BOATS</div>
    <div class="photo ph-boat" role="img" aria-label="Charter boat anchored in shallow turquoise sea"></div>
    <div class="copy"><span class="bold">Private Boat Charters</span><span class="light">In Grand Cayman</span><span class="sub">Come visit the stingrays with us!</span></div>
    <span class="cta">Learn More <svg width="13" height="13" viewBox="0 0 14 14"><circle cx="7" cy="7" r="7" fill="#2b1a00"/><path d="M3.5 7h6M7 4.5 9.5 7 7 9.5" stroke="#fff" stroke-width="1.8" fill="none"/></svg></span>
  </div>

  <div class="banner mini" style="left:239px;top:1362px">
    <div class="photo ph-boat" role="img" aria-label="Charter boat anchored in shallow turquoise sea"></div>
    <div class="copy"><span class="light">Private Boat</span><span class="bold">Charters in</span><span class="bold">Grand Cayman</span></div>
  </div>
  <div class="banner mini" style="left:590px;top:1362px">
    <div class="photo ph-pool" role="img" aria-label="Family snorkeling underwater in clear turquoise water"></div>
    <div class="copy"><span class="light">Private Boat</span><span class="bold">Charters in</span><span class="bold">Grand Cayman</span></div>
  </div>
  <div class="banner mini" style="left:941px;top:1362px">
    <div class="photo ph-reef" role="img" aria-label="Snorkelers swimming over a green reef"></div>
    <div class="copy"><span class="light">Private Boat</span><span class="bold">Charters in</span><span class="bold">Grand Cayman</span></div>
  </div>

</div>
</body>
</html>
```